Personal Training Studio needs small flyer design

My Personal Training Studio is looking to offer local high end clothes shops the option to offer their customers free Personal Training at our studio. It will be a small flyer (more a slip - landscape) that can be put into customers shopping bags once they have purchased an item from the store.
It is being marketed as a Local Fitness Initiative which is called "Be Fit In Your Clothes" The idea is to come from a "Be Fit" health perspective but also "Fit into your clothes" from the clothes shops perspective. Perhaps the "Be" in a different colour to the rest of the title. I would like my company logo and colours to be used, plus the address of the of the studio (see website - www.harbourlane7strength.co.uk). Flyer can be double sided

Target Market(s)

High end clothing shops

Industry/Entity Type

Training

Requirements
Must have
• Reference to the fact that the voucher is offering a FREE Personal Training session. Contact us to book yours today.

```html
<!DOCTYPE html>
<html lang="en">
<head>
<meta charset="utf-8">
<title>Be Fit – Free Session Flyer</title>
<link href="https://fonts.googleapis.com/css2?family=Arimo:wght@400;700&family=Tinos&display=swap" rel="stylesheet">
<style>
  :root {
    --paper: #ffffff;
    --ink: #111111;
    --brand-navy: #2b2d5e;
    --brand-teal: #3fb3ae;
    --skin-light: #e2b79a;
    --skin-mid: #c89274;
    --skin-shadow: #9e6c53;
    --denim: #4a5f7a;
    --denim-dark: #2f3f55;
  }
  * { margin: 0; padding: 0; box-sizing: border-box; }
  html, body {
    width: 1200px;
    height: 801px;
    overflow: hidden;
    background: var(--paper);
  }
  .flyer {
    position: relative;
    width: 1200px;
    height: 801px;
    background: var(--paper);
    color: var(--ink);
    font-family: "Arimo", Arial, sans-serif;
  }
  .hero-photo {
    position: absolute;
    left: 0;
    top: 0;
    width: 480px;
    height: 801px;
    background:
      linear-gradient(180deg,
        var(--skin-light) 0%,
        var(--skin-mid) 45%,
        var(--skin-shadow) 70%,
        var(--denim) 82%,
        var(--denim-dark) 100%);
  }
  .copy {
    position: absolute;
    left: 531px;
    top: 62px;
    width: 640px;
  }
  .headline {
    font-size: 47px;
    line-height: 52px;
    font-weight: 400;
    text-transform: uppercase;
    letter-spacing: 0.3px;
  }
  .title {
    font-family: "Tinos", "Times New Roman", serif;
    font-size: 96px;
    line-height: 1;
    font-weight: 400;
    margin-top: 28px;
  }
  .tagline {
    font-size: 30px;
    line-height: 37px;
    margin-top: 30px;
    text-transform: uppercase;
  }
  .offer {
    font-size: 24.5px;
    line-height: 30px;
    margin-top: 50px;
    text-transform: uppercase;
  }
  .studio-name {
    position: absolute;
    left: 531px;
    top: 620px;
    display: flex;
    align-items: center;
    gap: 22px;
    font-size: 46px;
    font-weight: 700;
    color: var(--brand-navy);
    text-transform: uppercase;
    letter-spacing: 1px;
  }
  .studio-mark {
    width: 34px;
    height: 34px;
    background: var(--brand-teal);
  }
</style>
</head>
<body>
  <main class="flyer">
    <div class="hero-photo" role="img" aria-label="Photo of a muscular shirtless man in jeans, shown from chest to hips"></div>

    <section class="copy">
      <h1 class="headline">Make the<br>right call…<br>Join us to</h1>
      <p class="title">BE FIT</p>
      <p class="tagline">Never get embarrased of your<br>shirt size!</p>
      <p class="offer">*Come for a free session with this flyer!<br>Contact us to book yours today.</p>
    </section>

    <div class="studio-name">
      <span class="studio-mark"></span>
      <span>Harbour Lane 7 Strength</span>
    </div>
  </main>
</body>
</html>
```